Quelindra - Step Into Bloom! Business Card

We are bringing an amazing new system of dance to Australia and need a nifty, eye-catching little card that we can give to everyone to get them to come to class.

It needs a bit of information about Quelindra, along with contact details and a space for us to write a note for people about the next class.

Target Market(s)

30+ people that enjoy dance and are interested in self-development, meeting people and getting more out of life.

Industry/Entity Type

Business

Requirements
Must have
• Double sided in colour

A beautiful, simple design that indicates movement and is modern, fresh and uplifting.

The attached Quelindra logo

Text for the front :

Quelindra - the Step Into Bloom

Dance from your heart and feel your life open.

Regular classes in Sydney and Canberra with Maren Hollis and Ernesto Varga

Text for the back :

Quelindra ignites our vital spark for life and awakens our innate potential for pleasurable, joyful, heartfelt living through dance, music and authentic connection.

Ernesto and Maren are committed to offering authentic, supportive and inspiring spaces for your growth through Quelindra.

Contact us on maren@quelindra.com.au - evtrusk@zentromail.net or 0472 318 904.

www.quelindra.com.au

Nice to have
• Some movement in the design

Use some of the photos attached in some form - could be faded, incorporated into design etc.

Creative use of the logo - integrating it within the design - e.g perhaps using it as the O in Quelindra,
Should not have
• Not a lot of black

```html
<!DOCTYPE html>
<html lang="en">
<head>
<meta charset="utf-8">
<title>Quelindra – Business Card</title>
<link rel="stylesheet" href="https://fonts.googleapis.com/css2?family=Roboto+Condensed:ital,wght@0,300;0,400;0,700;1,400&family=Roboto:wght@300&display=swap">
<style>
  :root {
    --backdrop: #2c2f30;
    --card: #ffffff;
    --plum: #93278f;
    --plum-soft: #b780b5;
    --lilac: #e6d3e5;
    --ink: #2a2a2a;
    --mist: #d8d8da;
  }
  html, body { margin: 0; padding: 0; }
  body {
    width: 1200px; height: 1200px; overflow: hidden;
    background: var(--backdrop);
    font-family: "Roboto Condensed", "Arial Narrow", sans-serif;
    color: var(--ink);
  }
  .stage {
    position: relative; width: 1280px; height: 1280px;
    transform: scale(0.9375); transform-origin: 0 0;
  }
  .card {
    position: absolute; top: 451px; width: 560px; height: 336px;
    background: var(--card); overflow: hidden;
  }
  .card--front { left: 73px; }
  .card--back { left: 674px; }
  .card svg.sweep { position: absolute; inset: 0; width: 560px; height: 336px; }

  /* front */
  .title-block { position: absolute; right: 38px; top: 34px; text-align: right; }
  .title-block .brand {
    display: block; font-size: 20px; font-weight: 400; color: var(--ink);
    text-align: left; margin-left: 22px; line-height: 1;
  }
  .title-block h1 {
    margin: 2px 0 0; font-size: 35px; font-weight: 700; color: var(--plum);
    line-height: 1; letter-spacing: -0.3px;
  }
  .title-block .tagline {
    margin: 3px 0 0; font-family: "Roboto", sans-serif; font-weight: 300;
    font-size: 13.5px; color: #444;
  }
  .logo-mark {
    position: absolute; left: 364px; top: 138px; width: 146px; height: 140px;
    display: flex; align-items: center; justify-content: center; gap: 8px;
  }
  .logo-mark .dot { width: 14px; height: 14px; border-radius: 50%; background: var(--plum); }
  .logo-mark .name { font-size: 22px; font-weight: 700; color: var(--ink); }
  .classes {
    position: absolute; right: 38px; top: 285px; margin: 0;
    font-size: 14.5px; color: #333;
  }
  .accent { color: var(--plum); }
  .accent-strong { color: var(--plum); font-weight: 700; }

  /* back */
  .photo-fade {
    position: absolute; inset: 0;
    background: linear-gradient(100deg, #cfcfd1 0%, #dadadc 45%, rgba(255,255,255,0.9) 75%, #fff 90%);
  }
  .about { position: absolute; left: 42px; top: 40px; width: 330px; font-size: 14.5px; line-height: 18px; color: #222; }
  .about p { margin: 0 0 11px; }
  .contact { position: absolute; left: 42px; top: 239px; font-size: 14.5px; line-height: 18px; color: #222; }
  .contact p { margin: 0; }
  .contact .lead { color: var(--plum); font-weight: 700; font-size: 16px; }
  .contact .web { color: var(--plum); font-style: italic; }
</style>
</head>
<body>
<div class="stage">

  <section class="card card--front" aria-label="Card front">
    <svg class="sweep" viewBox="0 0 560 336" aria-hidden="true">
      <defs>
        <linearGradient id="frontPlum" x1="0" x2="1" y1="0" y2="0">
          <stop offset="0" stop-color="#93278f"/>
          <stop offset="1" stop-color="#b06aad"/>
        </linearGradient>
        <linearGradient id="frontMist" x1="0" x2="1" y1="0" y2="0.2">
          <stop offset="0" stop-color="#d9bcd8"/>
          <stop offset="1" stop-color="#ffffff"/>
        </linearGradient>
      </defs>
      <path d="M0 0 H218 C232 60 200 120 130 185 C70 240 35 290 22 336 H0 Z" fill="url(#frontPlum)"/>
      <path d="M196 0 H218 C232 60 200 120 130 185 C70 240 35 290 22 336 H8 C20 270 90 190 160 120 C200 80 205 40 196 0 Z" fill="#c58fc3" opacity="0.7"/>
      <path d="M22 336 C35 290 70 240 130 185 C200 125 300 110 560 118 V0 H560 C420 10 300 60 230 120 C150 190 80 260 60 336 Z" fill="url(#frontMist)" opacity="0.55"/>
      <path d="M40 336 C60 270 120 200 200 150" stroke="#ffffff" stroke-width="3" fill="none" opacity="0.8"/>
    </svg>

    <div class="title-block">
      <span class="brand">Quelindra</span>
      <h1>the Step Into Bloom</h1>
      <p class="tagline">Dance from your heart and feel your life open</p>
    </div>

    <div class="logo-mark">
      <span class="dot"></span>
      <span class="name">Quelindra</span>
    </div>

    <p class="classes">Regular classes in <span class="accent">Sydney</span> and Canberra with <span class="accent-strong">Maren Hollis</span> and <span class="accent-strong">Ernesto Varga</span></p>
  </section>

  <section class="card card--back" aria-label="Card back">
    <div class="photo-fade" role="img" aria-label="Faded photo of dancers holding hands in class"></div>
    <svg class="sweep" viewBox="0 0 560 336" aria-hidden="true">
      <defs>
        <linearGradient id="backMist" x1="0" x2="1" y1="0" y2="0">
          <stop offset="0" stop-color="#ffffff" stop-opacity="0"/>
          <stop offset="0.5" stop-color="#f1e4f0"/>
          <stop offset="1" stop-color="#ffffff"/>
        </linearGradient>
        <linearGradient id="backPlum" x1="0" x2="1" y1="0" y2="0">
          <stop offset="0" stop-color="#b780b5"/>
          <stop offset="1" stop-color="#93278f"/>
        </linearGradient>
      </defs>
      <path d="M380 0 H560 V336 H540 C535 290 510 240 470 190 C430 140 385 80 380 0 Z" fill="url(#backMist)"/>
      <path d="M362 0 H380 C385 80 430 140 470 190 C510 240 535 290 540 336 H560 V336 H558 C552 285 525 230 480 178 C425 118 370 70 362 0 Z" fill="url(#backPlum)"/>
      <path d="M538 336 C532 290 505 240 465 192" stroke="#d7a9d5" stroke-width="3" fill="none"/>
    </svg>

    <div class="about">
      <p>Quelindra ignites our vital spark for life and awakens our innate potential for pleasurable, joyful heartfelt living through dance, music and authentic connection.</p>
      <p>Ernesto and Maren are committed to offering authentic supportive and inspiring spaces for your growth through Quelindra.</p>
    </div>

    <div class="contact">
      <p><span class="lead">Contact us on</span> maren@quelindra.com.au</p>
      <p>evtrusk@zentromail.net or 0472 318 904</p>
      <p class="web">www.quelindra.com.au</p>
    </div>
  </section>

</div>
</body>
</html>
```